Pinecrest Artisan League Membership

UPDATED files - 06/03/2021
Digital brochure needed for construction contractor related nonprofit organization.
Document will be primarily for digital viewing with potential for print version. Should be branded with our branding (logo attached). This is intended to be a multiple page document, plan to print and web (email) use. Standard Letter size document 8.5 x 11 inch
Portrait format preferred
The attached project brief includes a cover, 4 internal pages, and a back cover. This is flexible pending design layout
Target Market(s)
Residential construction business owners
Requirements
Must have
- See attached brief.Orange color palette: RGB: (253,153,0)
Nice to have
- See attached bief
Should not have
- No suit or ties. button up shirt okay, but not white collar worker.

```html
<!DOCTYPE html>
<html lang="en">
<head>
<meta charset="utf-8">
<title>Pinecrest Artisan League – Membership Brochure</title>
<link href="https://fonts.googleapis.com/css2?family=Montserrat:wght@400;500;600;700;800&display=swap" rel="stylesheet">
<style>
  :root{
    --orange:#fd9900;
    --ink:#3a3a3c;
    --text:#4a4a4a;
    --paper:#ffffff;
    --stage:#dcdce0;
    --card-line:#ececec;
  }
  *{box-sizing:border-box;margin:0;padding:0}
  html,body{width:669px;height:1200px;overflow:hidden}
  body{background:var(--stage);font-family:'Montserrat',sans-serif;color:var(--text);position:relative}

  .page{position:absolute;background:var(--paper);overflow:hidden;box-shadow:0 6px 18px rgba(0,0,0,.12)}
  .front-solo{left:206px;top:24px;width:256px;height:331px}
  .spread{position:absolute;left:34.5px;width:600px;height:388px;display:flex;box-shadow:0 6px 18px rgba(0,0,0,.12)}
  .spread-inner{top:379px}
  .spread-outer{top:791px}
  .spread .leaf{position:relative;width:300px;height:388px;background:var(--paper);overflow:hidden}
  .spread .leaf + .leaf{border-left:1px solid #e6e6e6}

  /* cover */
  .cover-photo{position:absolute;border-radius:50%;background:linear-gradient(135deg,#4a4036 0%,#6b5234 45%,#c8762a 72%,#3a3024 100%)}
  .front-solo .cover-photo{left:22px;top:92px;width:256px;height:256px}
  .leaf .cover-photo{left:26px;top:140px;width:300px;height:300px}
  .wordmark{position:absolute;display:flex;align-items:center;gap:5px;font-weight:800;color:var(--ink);text-transform:uppercase;line-height:1.05;letter-spacing:.3px}
  .wordmark .dot{flex:none;border-radius:50%;background:var(--orange)}
  .cover-mark{left:20px;top:22px;font-size:12px}
  .cover-mark .dot{width:12px;height:12px}
  .front-solo .cover-mark{left:17px;top:19px;font-size:10.5px}
  .front-solo .cover-mark .dot{width:10px;height:10px}

  /* inner pages */
  .h{font-weight:700;font-size:7px;color:var(--ink);text-transform:uppercase;letter-spacing:.3px}
  .h::after{content:"";display:block;width:18px;height:1.5px;background:var(--orange);margin-top:2px}
  .sub{font-weight:700;font-size:5.5px;color:var(--orange);text-transform:uppercase;margin-top:4px}
  .p{font-size:4.6px;line-height:1.5;color:var(--text);margin-top:3px}
  .block{position:absolute}
  .card{position:absolute;background:var(--paper);border:1px solid var(--card-line);box-shadow:0 2px 5px rgba(0,0,0,.08);padding:7px}
  .photo{position:absolute;border-bottom:2px solid var(--orange)}
  .photo-site{background:linear-gradient(135deg,#3b2a1c 0%,#6d5a3e 40%,#cfd3d6 65%,#f2f2f2 80%,#5c4a33 100%)}
  .photo-city{background:linear-gradient(180deg,#1d2438 0%,#e38a2f 38%,#3a3346 55%,#14182a 100%)}

  .values{position:absolute;left:18px;top:318px;width:264px;display:grid;grid-template-columns:repeat(3,1fr);row-gap:8px;column-gap:6px}
  .value{display:flex;align-items:center;gap:5px;font-size:4.6px;line-height:1.35;color:var(--text)}
  .ring{flex:none;width:14px;height:14px;border:1.5px solid var(--orange);border-radius:50%}

  .services{position:absolute;left:18px;top:112px;width:264px;display:grid;grid-template-columns:repeat(4,1fr);gap:4px}
  .item{display:flex;align-items:center;gap:4px;font-size:4.6px;line-height:1.3;color:var(--text)}
  .bullet{flex:none;width:7px;height:7px;border-radius:50%;background:var(--orange)}
  .features{position:absolute;left:18px;top:318px;width:264px;display:grid;grid-template-columns:1fr 1fr;gap:6px 12px}

  /* back cover */
  .back-block{position:absolute;left:62px;top:268px;width:176px;text-align:center}
  .back-mark{position:static;justify-content:center;font-size:9px}
  .back-mark .dot{width:9px;height:9px}
  .contact-icons{display:flex;justify-content:center;gap:4px;margin:10px 0 6px}
  .contact-icons svg{width:10px;height:10px}
  .contact-line{font-size:5.5px;line-height:1.6;color:var(--ink);font-weight:500}
</style>
</head>
<body>

<!-- Front cover, standalone -->
<section class="page front-solo" aria-label="Front cover">
  <div class="cover-photo" role="img" aria-label="Photo of two construction workers in hard hats and safety vests reviewing plans"></div>
  <div class="wordmark cover-mark"><span class="dot"></span><span>Pinecrest<br>Artisan League</span></div>
</section>

<!-- Inner spread -->
<section class="spread spread-inner" aria-label="Inside spread">
  <article class="leaf">
    <div class="block" style="left:18px;top:16px;width:264px">
      <h2 class="h">About Us</h2>
      <p class="p">PAL is organized as a 501c6 membership organization supported by a 501c3 charitable foundation. Our foundation allows us to provide access to training and resources to an underserved community of contractors, helping them grow sustainable businesses. We invite you to join a community that shares ideas, lessons learned, proven practices and insights with other industry leaders.</p>
    </div>
    <div class="card" style="left:18px;top:92px;width:128px;height:70px">
      <h3 class="h">Mission</h3>
      <p class="p">To promote, educate and advance a diverse contractor community by providing pathways of accessibility to help build a stronger foundation for a better future.</p>
    </div>
    <div class="card" style="left:154px;top:120px;width:128px;height:62px">
      <h3 class="h">Vision</h3>
      <p class="p">To become the preferred organization for construction contractors striving to be the best in their trade through education, training and ongoing development.</p>
    </div>
    <div class="photo photo-site" style="left:18px;top:190px;width:264px;height:70px" role="img" aria-label="Photo of a white hard hat resting on rolled construction blueprints"></div>
    <div class="block" style="left:18px;top:268px;width:264px">
      <h2 class="h">Diversity, Equity &amp; Inclusion</h2>
      <p class="p">PAL promotes and encourages open dialogue and positive working environments for all identity groups, to thrive within a contractor community and facilitate a more inclusive and resilient future.</p>
    </div>
    <div class="block" style="left:18px;top:302px"><h2 class="h">Core Values</h2></div>
    <div class="values">
      <div class="value"><span class="ring"></span>Empower through learning &amp; development</div>
      <div class="value"><span class="ring"></span>Strengthen &amp; sustain the industry</div>
      <div class="value"><span class="ring"></span>Act with integrity, respect and honesty</div>
      <div class="value"><span class="ring"></span>Promote diversity, equity and inclusion throughout the industry</div>
      <div class="value"><span class="ring"></span>Build partnerships to benefit underserved communities</div>
    </div>
  </article>

  <article class="leaf">
    <div class="block" style="left:18px;top:16px;width:264px">
      <h2 class="h">Technical Assistance</h2>
      <p class="p">One of our primary goals is to provide technical assistance to the contractor community based on individual level of competency. We understand that contractors' strengths lie in their knowledge of their trade, and business skills must be developed around their strengths.</p>
      <p class="p">The importance for contractors to understand how to use and implement current technology, acquire new skills and expand existing capacity lies therein that it helps business owners become more competitive in their market so they can ultimately increase their revenue and strengthen their business.</p>
      <p class="p">Technical assistance may take many forms. Examples we provide include teaching skills, building capacity or creating change, such as:</p>
    </div>
    <div class="services">
      <div class="item"><span class="bullet"></span>Business &amp; strategic planning</div>
      <div class="item"><span class="bullet"></span>Marketing and communications</div>
      <div class="item"><span class="bullet"></span>Computer technology</div>
      <div class="item"><span class="bullet"></span>Legal and accounting services</div>
    </div>
    <div class="photo photo-city" style="left:18px;top:134px;width:264px;height:58px" role="img" aria-label="Photo of a city skyline at dusk with warm orange sky"></div>
    <div class="block" style="left:18px;top:200px;width:264px">
      <h2 class="h">Safety &amp; Compliance</h2>
      <h3 class="sub">SafeLogbook</h3>
      <p class="p">SafeLogbook is a secure, web-based application that enables employers to create each state's first report of injury, track injuries and view injury metrics in real time. Print, share or email logs and forms. Works with all devices: computers, tablets and smartphones, and automatically generates benchmark figures.</p>
      <h3 class="sub">CrewGuard</h3>
      <p class="p">Our partnership with CrewGuard gives you the tools you need to protect your workers, meet compliance requirements and create a positive workplace environment. Their staff of safety professionals and trainers has helped thousands of contractors save money and improve efficiency.</p>
      <p class="p">Included in the mobile app are the following:</p>
    </div>
    <div class="features">
      <div class="item"><span class="bullet"></span>Over 1,200 bilingual (Spanish/English) safety lessons with digital signoff rosters</div>
      <div class="item"><span class="bullet"></span>An online form builder to create job and equipment-specific inspection forms</div>
      <div class="item"><span class="bullet"></span>Mobile-accessible document storage repository</div>
      <div class="item"><span class="bullet"></span>Live monthly webinars addressing safety topics</div>
    </div>
  </article>
</section>

<!-- Outer spread: back cover + front cover -->
<section class="spread spread-outer" aria-label="Outside spread">
  <article class="leaf">
    <div class="back-block">
      <div class="wordmark back-mark"><span class="dot"></span><span>Pinecrest<br>Artisan League</span></div>
      <div class="contact-icons">
        <svg viewBox="0 0 10 10" aria-label="Phone"><circle cx="5" cy="5" r="4.5" fill="none" stroke="var(--orange)" stroke-width=".8"/><path d="M3.4 3c.3-.3.6-.2.8.1l.4.6c.1.2 0 .4-.1.5l-.3.2c.3.6.7 1 1.3 1.3l.2-.3c.1-.2.3-.2.5-.1l.6.4c.3.2.3.5.1.8-.4.5-1 .6-1.6.2C4.3 6.3 3.7 5.7 3.3 4.9 3 4.2 3 3.5 3.4 3z" fill="var(--orange)"/></svg>
        <svg viewBox="0 0 10 10" aria-label="Email"><circle cx="5" cy="5" r="4.5" fill="none" stroke="var(--orange)" stroke-width=".8"/><rect x="2.8" y="3.5" width="4.4" height="3" fill="none" stroke="var(--orange)" stroke-width=".6"/><path d="M2.8 3.5 5 5.2 7.2 3.5" fill="none" stroke="var(--orange)" stroke-width=".6"/></svg>
        <svg viewBox="0 0 10 10" aria-label="Website"><circle cx="5" cy="5" r="4.5" fill="none" stroke="var(--orange)" stroke-width=".8"/><circle cx="5" cy="5" r="2.4" fill="none" stroke="var(--orange)" stroke-width=".6"/><ellipse cx="5" cy="5" rx="1" ry="2.4" fill="none" stroke="var(--orange)" stroke-width=".5"/><path d="M2.6 5h4.8" stroke="var(--orange)" stroke-width=".5"/></svg>
      </div>
      <p class="contact-line">(555) 018-2746</p>
      <p class="contact-line">info@pinecrestartisanleague.org</p>
      <p class="contact-line">www.pinecrestartisanleague.org</p>
    </div>
  </article>
  <article class="leaf">
    <div class="cover-photo" role="img" aria-label="Photo of two construction workers in hard hats and safety vests reviewing plans"></div>
    <div class="wordmark cover-mark"><span class="dot"></span><span>Pinecrest<br>Artisan League</span></div>
  </article>
</section>

</body>
</html>
```